The amber lantern with an elephant incorporated in the background

Target Market(s)

Real estate

Industry/Entity Type

Real Estate

Contact Information for Business Card

On back on want my name & number
In front I want the business name, "the amber lantern", below to say staging & design

Logo Text

The amber lantern

Font styles to use
Serif

Colors
000000

Requirements
Must have
• I want an elephant behind the writing in gold transperant

```html
<!DOCTYPE html>
<html lang="en">
<head>
<meta charset="utf-8">
<title>The Amber Lantern – Business Cards</title>
<link rel="stylesheet" href="https://fonts.googleapis.com/css2?family=Lato:wght@700&family=Lora:wght@400&display=swap">
<style>
  :root {
    --page: #ece7e1;
    --card-black: #050606;
    --gold: #d4ad63;
    --gold-rule: #1a1712;
    --brand-orange: #f2a52a;
    --elephant-gold: rgba(150, 115, 40, 0.55);
    --white: #ffffff;
    --ink: #2a2419;
  }
  html, body {
    margin: 0;
    padding: 0;
    width: 1200px;
    height: 1200px;
    overflow: hidden;
    background: var(--page);
  }
  .canvas {
    position: relative;
    width: 1200px;
    height: 1200px;
  }
  .card {
    position: absolute;
    top: 200px;
    width: 460px;
    height: 800px;
    background: var(--card-black);
    overflow: hidden;
    box-shadow: 0 6px 18px rgba(0,0,0,0.18);
  }
  .card--front { left: 110px; }
  .card--back  { left: 630px; }

  .band {
    position: absolute;
    left: 0;
    right: 0;
    background: var(--gold);
  }
  .band--top {
    top: 0;
    height: 140px;
  }
  .band--bottom {
    bottom: 0;
    height: 170px;
  }
  .band__rule {
    position: absolute;
    left: 0;
    right: 0;
    height: 5px;
    background: var(--gold-rule);
  }
  .band--top .band__rule { bottom: 10px; }
  .band--bottom .band__rule { top: 10px; }

  .tagline {
    position: absolute;
    left: 0;
    right: 0;
    bottom: 60px;
    margin: 0;
    text-align: center;
    font-family: "Lora", Georgia, serif;
    font-size: 30px;
    color: var(--ink);
    letter-spacing: 0.5px;
  }

  .elephant-art {
    position: absolute;
    left: 30px;
    top: 250px;
    width: 400px;
    height: 250px;
    border-radius: 45% 50% 30% 30%;
    background: radial-gradient(ellipse at 45% 45%, var(--elephant-gold) 0%, rgba(150,115,40,0.35) 55%, rgba(150,115,40,0) 78%);
  }
  .brand-name {
    position: absolute;
    left: 0;
    right: 0;
    top: 318px;
    margin: 0;
    text-align: center;
    font-family: "Lato", Arial, sans-serif;
    font-weight: 700;
    color: var(--brand-orange);
    line-height: 1.1;
    text-transform: uppercase;
  }
  .brand-name__the {
    display: block;
    font-size: 42px;
  }
  .brand-name__rule {
    display: block;
    width: 340px;
    height: 2px;
    margin: 4px auto 6px;
    background: var(--brand-orange);
    opacity: 0.7;
  }
  .brand-name__main {
    display: block;
    font-size: 42px;
  }

  .contact {
    position: absolute;
    left: 0;
    right: 0;
    top: 350px;
    text-align: center;
  }
  .contact__name {
    font-family: "Lato", Arial, sans-serif;
    font-weight: 700;
    font-size: 46px;
    color: var(--white);
    letter-spacing: 0.5px;
    margin: 0;
  }
  .contact__tel {
    font-family: "Lora", Georgia, serif;
    font-size: 26px;
    color: var(--white);
    margin: 14px 0 0;
    letter-spacing: 1px;
  }
</style>
</head>
<body>
<div class="canvas">

  <section class="card card--front">
    <div class="band band--top"><span class="band__rule"></span></div>
    <div class="elephant-art" role="img" aria-label="Semi-transparent gold elephant illustration behind the business name"></div>
    <h1 class="brand-name">
      <span class="brand-name__the">The</span>
      <span class="brand-name__rule"></span>
      <span class="brand-name__main">Amber Lantern</span>
    </h1>
    <div class="band band--bottom"><span class="band__rule"></span></div>
    <p class="tagline">Staging &amp; Design</p>
  </section>

  <section class="card card--back">
    <div class="band band--top"><span class="band__rule"></span></div>
    <div class="contact">
      <p class="contact__name">JOHN DOE</p>
      <p class="contact__tel">Tel: 123-456-7890</p>
    </div>
    <div class="band band--bottom"><span class="band__rule"></span></div>
    <p class="tagline">Staging &amp; Design</p>
  </section>

</div>
</body>
</html>
```